Professional Engineering Web Design

Project Brief: Website Redesign for Mechanical Design Consultancy
Project Overview
I want to update and improve my current website to create a more professional, modern, and high-credibility online presence for my mechanical design consultancy.

Current site: https://valtrobuild.design/

The new website must communicate expertise, precision, and trust—matching the standard of top engineering and product design agencies.

Reference Websites (Style + Structure Inspiration)
These represent the quality, cleanliness, and professionalism I want to achieve:

https://plinthformworks.com/
https://www.zorvanta.com/
https://quellory-uk.com/
Brand Look
Professional, modern, engineering-focused aesthetic
Clean layouts and strong typography
High-quality imagery conveying precision, innovation, and mechanical expertise
Colour scheme and styling must follow my existing logo (attached in project)
Platform Requirements
The website must be built on WordPress
Should use a clean, flexible theme or modern page builder (Elementor, Gutenberg, Bricks, or similar)
Avoid overly complex custom coding so I can easily edit content later
Final deliverable must allow me to manage and update content without developer assistance
Functionality
Fast-loading, lightweight, and smooth user experience
Clean animations and transitions similar to the reference sites
Fully mobile responsive
Clear navigation and strong visual hierarchy
Contact forms optimised for lead generation
Optional: subtle scroll effects, case study sliders, icon animations, etc.
SEO Aspirations
Developer should recommend and implement a modern SEO strategy
Proper on-page SEO setup (titles, meta, schema, alt tags, heading structure)
Optimised site architecture for ranking and crawling
Aim: Generate leads through improved visibility and keyword targeting
Optional but useful: plain review badge Analytics, plain review badge Search Console setup
User Journeys
(Recommended structure)

The site should be crafted around clear, intuitive journeys for each type of visitor:

Potential new clients
Quickly understand what services I offer
View examples of past work / case studies
See credibility indicators (process, expertise, industries served)
Easily contact me or request a project discussion
Returning clients
Access updated portfolio items
Find contact details or book follow-up work easily
General visitors discovering through SEO
Be guided to core service areas
Understand my value proposition quickly
Be invited to learn more or make contact
The developer should design the structure to support these journeys smoothly.

Maintenance Expectations
Website will be maintained by me, so it should be easy to update using relatively basic WordPress skills
Use modular templates and simple backend structure
Avoid unnecessary plugins
Provide brief handover documentation if required
Hosting Preferences
Site is currently hosted via a family member
Open to discussing moving to a paid, reliable hosting provider if preferable for performance and maintainability
Developer may advise on the best hosting setup for WordPress
Content
Most content can be taken from the existing website
Developer is welcome to suggest improvements to structure, layout, and imagery
Must remain easy for me to edit or add new content later (e.g., new projects)
Deliverables
Fully built WordPress website
Clean, professional, modern design inspired by the reference sites
Mobile-responsive across all devices
SEO-ready structure and optimisations
Transfer of website and admin rights
Any design assets, templates, or documentation used

```html
<!DOCTYPE html>
<html lang="en">
<head>
<meta charset="utf-8">
<title>Valtro Build – Mechanical CAD Design</title>
<link href="https://fonts.googleapis.com/css2?family=Inter:ital,wght@0,400;0,500;0,600;0,700;0,800;1,400&display=swap" rel="stylesheet">
<style>
:root{
  --blue:#2f58ec;
  --blue-soft:#8ea4f4;
  --ink:#14151c;
  --text:#2a2b33;
  --muted:#55575f;
  --tag:#e2e5f3;
  --grey-band:#eceaee;
  --steel:#3c3f4a;
  --navy:#1c1d33;
  --white:#ffffff;
}
*{margin:0;padding:0;box-sizing:border-box}
html,body{width:1200px;height:4286px;overflow:hidden}
body{position:relative;background:var(--white);font-family:'Inter',sans-serif;color:var(--text)}
.abs{position:absolute}
.center{text-align:center}

/* top bar + nav */
.topbar{left:466px;top:0;width:734px;height:22px;background:var(--blue);color:var(--white);font-size:11px;display:flex;align-items:center;gap:0;padding-left:28px}
.topbar span{display:flex;align-items:center;gap:6px;padding:0 18px;border-right:1px solid rgba(255,255,255,.45)}
.topbar span:last-child{border-right:none}
.nav{left:0;top:22px;width:1200px;height:73px;background:var(--white)}
.nav-links{left:385px;top:52px;display:flex;gap:0;font-size:15px;color:var(--ink)}
.nav-links a{color:inherit;text-decoration:none;position:absolute;white-space:nowrap}
.search{left:797px;top:42px;width:260px;height:40px;border:1px solid #cfd0d6;border-radius:20px;font-size:14px;color:#a9abb2;padding:11px 26px}
.search svg{position:absolute;right:14px;top:9px}
.logo-badge{left:133px;top:-22px;width:166px;height:166px;border-radius:50%;background:var(--white);z-index:5;display:flex;flex-direction:column;align-items:center;justify-content:flex-end;padding-bottom:30px}
.brand-name{font-size:34px;font-weight:600;color:var(--blue);letter-spacing:3px;line-height:1}
.brand-sub{font-size:9px;font-weight:600;color:var(--blue);letter-spacing:.6px;margin-top:4px}
.logo-dot{width:44px;height:44px;border-radius:50%;background:var(--blue);margin-bottom:10px}

/* hero */
.hero{left:0;top:95px;width:1200px;height:637px;background:linear-gradient(100deg,#3d4c6b 0%,#6a7c98 35%,#2b3246 62%,#4d5d7e 100%);overflow:hidden}
.hero-shade{inset:0;background:linear-gradient(180deg,rgba(20,25,40,.35),rgba(20,25,40,.15))}
.hero-title{left:0;top:222px;width:1200px;font-size:66px;font-weight:800;color:var(--white);letter-spacing:.5px}
.hero-sub{left:205px;top:310px;width:790px;font-size:15px;line-height:21px;color:var(--white)}
.btn-dark{left:363px;top:374px;width:228px;height:47px;border-radius:24px;background:#0e0f15;color:var(--white);font-size:15px;font-weight:600;display:flex;align-items:center;padding-left:65px}
.btn-dark i{position:absolute;left:20px;top:15px;width:17px;height:17px;border-radius:50%;background:var(--blue)}
.btn-ghost{left:609px;top:374px;width:230px;height:47px;border-radius:24px;border:1px solid rgba(255,255,255,.8);color:var(--white);font-size:15px;font-weight:600;display:flex;align-items:center;justify-content:center}

/* headings */
.tag{background:var(--tag)}
.h-section{font-weight:800;color:var(--ink);letter-spacing:.3px}
.lead{font-size:15px;line-height:21px;color:var(--ink)}

/* about */
.about-photo{left:150px;top:907px;width:404px;height:428px;border-radius:200px 200px 0 0;background:radial-gradient(circle at 50% 45%,#2f58ec 0 58%,transparent 59%),linear-gradient(180deg,#f0f1f5,#fff)}
.about-photo .people{position:absolute;left:12px;top:0;width:380px;height:428px;background:linear-gradient(180deg,#e48a2c 0%,#c7653b 40%,#59606f 100%);opacity:.55;border-radius:190px 190px 0 0}
.about-h{left:657px;top:936px;display:flex;align-items:center;gap:14px;font-size:34px;font-weight:800;color:var(--ink)}
.about-h i{width:40px;height:40px;border-radius:50%;background:var(--blue);display:block}
.about-copy{left:657px;top:1000px;width:400px;font-size:13px;line-height:23px;color:var(--text)}
.about-copy p{margin-bottom:22px}
.btn-blue{background:var(--blue);color:var(--white);border-radius:24px;font-size:15px;font-weight:600;display:flex;align-items:center;justify-content:center}

/* stats */
.stats-band{left:0;top:1331px;width:1200px;height:399px;background:linear-gradient(180deg,#ffffff 0%,#c9ccd3 20%,#7b808c 55%,#4b4f59 80%,#9ea2ab 100%)}
.stat{top:1403px;width:193px;height:105px;background:var(--white);border-radius:4px;box-shadow:0 2px 6px rgba(0,0,0,.12)}
.stat::before{content:"";position:absolute;left:28px;top:15px;width:3px;height:76px;background:var(--blue)}
.stat b{position:absolute;left:40px;top:8px;font-size:50px;font-weight:600;color:var(--ink);letter-spacing:-1px}
.stat span{position:absolute;left:40px;top:76px;font-size:15px;color:var(--muted)}

/* work */
.work-card{top:1962px;width:286px;height:439px;background:var(--blue);border-radius:3px;overflow:hidden;color:var(--white);text-align:center}
.work-img{position:absolute;left:0;top:0;width:286px;height:220px}
.icon-disc{position:absolute;left:93px;top:170px;width:100px;height:100px;border-radius:50%;background:var(--white);display:flex;align-items:center;justify-content:center}
.work-card h3{position:absolute;left:0;top:288px;width:286px;font-size:19px;font-weight:700}
.work-card p{position:absolute;left:20px;top:316px;width:246px;font-size:13px;line-height:21px}
.arrow{width:54px;height:54px;border-radius:50%;display:flex;align-items:center;justify-content:center}
.arrow.prev{background:var(--blue-soft)}
.arrow.next{background:var(--white);border:1.5px solid #9ea0a8}

/* expertise */
.exp-band{left:0;top:2541px;width:1200px;height:600px;background:var(--grey-band)}
.exp-card{top:2762px;width:296px;height:255px;background:var(--white);border-radius:16px;text-align:center}
.exp-card .disc{position:absolute;left:98px;top:30px;width:100px;height:100px;border-radius:50%;background:var(--blue);display:flex;align-items:center;justify-content:center}
.exp-card h3{position:absolute;left:0;top:150px;width:100%;font-size:19px;font-weight:500;color:var(--ink)}
.exp-card p{position:absolute;left:20px;top:186px;width:256px;font-size:13px;line-height:21px;color:var(--muted)}

/* reviews */
.review{top:3561px;width:286px;height:358px;background:var(--white);border:1px solid #e4e5ea;text-align:center}
.review .badge{position:absolute;left:122px;top:-22px;width:42px;height:42px;border-radius:50%;background:var(--white);border:1px solid #d8d9de}
.review .stars{position:absolute;left:0;top:38px;width:100%;font-size:19px;letter-spacing:1px;color:var(--blue)}
.review blockquote{position:absolute;left:36px;top:74px;width:214px;font-size:9.6px;line-height:19.5px;font-style:italic;color:#62646b}
.review .avatar{position:absolute;left:119px;top:246px;width:48px;height:48px;border-radius:50%;background:linear-gradient(160deg,#c98a64,#5b3a2a)}
.review .who{position:absolute;left:0;top:302px;width:100%;font-size:13px;line-height:22px;color:var(--ink)}

/* footer */
.footer{left:0;top:3974px;width:1200px;height:312px;background:var(--navy);color:#c9cad6}
.footer h4{font-size:12px;font-weight:700;color:var(--white)}
.footer a{display:block;color:#c9cad6;text-decoration:none;font-size:12px}
</style>
</head>
<body>

<!-- top bar -->
<div class="abs topbar">
  <span><svg width="10" height="12" viewBox="0 0 10 12"><path d="M5 0a4 4 0 0 0-4 4c0 3 4 8 4 8s4-5 4-8a4 4 0 0 0-4-4zm0 5.5A1.5 1.5 0 1 1 5 2.5a1.5 1.5 0 0 1 0 3z" fill="#fff"/></svg>We're based in South Wales, UK.</span>
  <span><svg width="11" height="11" viewBox="0 0 24 24"><path d="M6.6 10.8a15 15 0 0 0 6.6 6.6l2.2-2.2c.3-.3.7-.4 1-.2 1.1.4 2.3.6 3.6.6.6 0 1 .4 1 1V20c0 .6-.4 1-1 1A17 17 0 0 1 3 4c0-.6.4-1 1-1h3.5c.6 0 1 .4 1 1 0 1.3.2 2.5.6 3.6.1.3 0 .7-.2 1z" fill="#fff"/></svg>+44 (0) 7700 900482</span>
  <span><svg width="11" height="11" viewBox="0 0 24 24"><path d="M2 11 22 2l-9 20-2-8z" fill="#fff"/></svg>info@valtrobuild.design</span>
</div>

<!-- nav -->
<header class="abs nav"></header>
<div class="abs logo-badge">
  <div class="logo-dot"></div>
  <div class="brand-name">valtro</div>
  <div class="brand-sub">MECHANICAL DESIGN</div>
</div>
<nav class="abs nav-links" style="left:0;top:52px">
  <a href="#" style="left:385px">Services</a>
  <a href="#" style="left:481px">Portfolio</a>
  <a href="#" style="left:576px">Process</a>
  <a href="#" style="left:668px">About</a>
</nav>
<div class="abs search">Search
  <svg width="22" height="22" viewBox="0 0 24 24" fill="none" stroke="#333" stroke-width="1.8"><circle cx="10" cy="10" r="7"/><path d="m15.5 15.5 6 6"/></svg>
</div>

<!-- hero -->
<section class="abs hero" role="img" aria-label="Engineers reviewing a 3D mechanical CAD model on a monitor in a workshop">
  <div class="abs hero-shade"></div>
</section>
<h1 class="abs hero-title center">MECHANICAL CAD DESIGN</h1>
<p class="abs hero-sub center">From concept to fully manufacturable product I provide expert mechanical design that solves complex en-gineering challenges with accuracyand efficiency.</p>
<a class="abs btn-dark"><i></i>Start Your Project</a>
<a class="abs btn-ghost">View Case Studies</a>
<svg class="abs" style="left:0;top:620px" width="1200" height="115" viewBox="0 0 1200 115" preserveAspectRatio="none">
  <path d="M0 55 C350 125 800 120 1200 30 V115 H0Z" fill="#3c3f4a"/>
  <path d="M0 20 C300 75 700 100 1200 35 V45 C800 115 300 115 0 62Z" fill="#2f58ec"/>
  <path d="M0 66 C350 130 800 125 1200 48 V115 H0Z" fill="#3c3f4a"/>
  <path d="M0 62 C350 128 800 135 1200 62 V115 H0Z" fill="#ffffff"/>
</svg>

<!-- intro heading -->
<h2 class="abs h-section center" style="left:0;top:790px;width:1200px;font-size:43px;line-height:49px">PRECISION RELIABILITY PRACTICAL</h2>
<div class="abs tag" style="left:438px;top:840px;width:324px;height:47px"></div>
<h2 class="abs h-section center" style="left:0;top:839px;width:1200px;font-size:43px;line-height:49px">ENGINEERING.</h2>

<!-- about -->
<div class="abs about-photo" role="img" aria-label="Two engineers in hi-vis vests and a hard hat reviewing plans on a laptop">
  <div class="people"></div>
</div>
<div class="abs about-h"><i></i>ABOUT US</div>
<div class="abs about-copy">
  <p>Owen Marsh is the Chief Engineer at Valtro Mechanical Design. He has 11 years experience working as a mechanical design engineer in multiple industries icluing high performance automotive,</p>
  <p>consumer products, medical, industrial plus many more. He has worked in multiple roles across a wide range of products.</p>
  <p>Valtro Build provides professional mechanical engineering &amp; product development support for companies that require accurate, productionready design. With experi-ence across multiple industries</p>
</div>
<a class="abs btn-blue" style="left:657px;top:1295px;width:230px;height:46px">Tell us about your ideas</a>

<!-- stats -->
<div class="abs stats-band" role="img" aria-label="Close-up of a machined metal gearbox assembly"></div>
<div class="abs stat" style="left:145px"><b>15+</b><span>Years Experience</span></div>
<div class="abs stat" style="left:384px"><b>200+</b><span>Projects Delivered</span></div>
<div class="abs stat" style="left:624px"><b>100%</b><span>Client Satisfaction</span></div>
<div class="abs stat" style="left:864px"><b>50+</b><span>Industries Served</span></div>

<!-- our work -->
<div class="abs tag" style="left:454px;top:1806px;width:293px;height:61px"></div>
<h2 class="abs h-section center" style="left:0;top:1806px;width:1200px;font-size:50px;line-height:60px">OUR WORK</h2>
<p class="abs lead center" style="left:270px;top:1884px;width:660px">Explore a range of projects demonstrating our expertise in CAD modeling, mechanical design, and engineering for manufacture.</p>

<div class="abs arrow prev" style="left:63px;top:2155px"><svg width="16" height="16" viewBox="0 0 16 16" fill="none" stroke="#1c1d33" stroke-width="2.4"><path d="M10 2 4 8l6 6"/></svg></div>
<div class="abs arrow next" style="left:1080px;top:2155px"><svg width="16" height="16" viewBox="0 0 16 16" fill="none" stroke="#2f58ec" stroke-width="2.4"><path d="m6 2 6 6-6 6"/></svg></div>

<article class="abs work-card" style="left:145px">
  <div class="work-img" role="img" aria-label="White performance car with custom alloy wheels on a road" style="background:linear-gradient(180deg,#7d8088,#c9cbd0 55%,#4a4c52)"></div>
  <div class="icon-disc"><svg width="48" height="48" viewBox="0 0 48 48" fill="none" stroke="#333" stroke-width="2"><circle cx="24" cy="24" r="19"/><circle cx="24" cy="24" r="5"/><path d="M24 5v14M24 29v14M5 24h14M29 24h14"/></svg></div>
  <h3>3-Piece Alloy Wheels</h3>
  <p>We have been working on a long term project to bring custom 3-piece Japanese style wheels to market since 2020.</p>
</article>
<article class="abs work-card" style="left:458px">
  <div class="work-img" role="img" aria-label="Driver racing a go-kart on a track" style="background:linear-gradient(180deg,#9aa0a6,#7b8088 50%,#5f6368)"></div>
  <div class="icon-disc"><svg width="48" height="48" viewBox="0 0 48 48" fill="none" stroke="#333" stroke-width="2"><path d="M6 32h36l-4-8H20l-4-6h-6z"/><circle cx="13" cy="36" r="4"/><circle cx="35" cy="36" r="4"/></svg></div>
  <h3>Go-Kart Simulator Design</h3>
  <p>Our client already had an existing product, but wanted it updating and refreshing to offer their cus-tomers a better product.</p>
</article>
<article class="abs work-card" style="left:771px">
  <div class="work-img" role="img" aria-label="Engineer in hi-vis inspecting electrical switchgear cabinets" style="background:linear-gradient(180deg,#6e747e,#a5a9ae 50%,#b8c23a 80%,#575b62)"></div>
  <div class="icon-disc"><svg width="48" height="48" viewBox="0 0 48 48" fill="none" stroke="#333" stroke-width="2"><rect x="6" y="12" width="26" height="24" rx="3"/><path d="M13 20v8M19 20v8M25 20v8"/><circle cx="37" cy="32" r="6"/></svg></div>
  <h3>Electrical Switchgear</h3>
  <p>In the UK a lot of electrical switch-gear in grid sub-stations are very old, many of them originating in the 60s. In this time maintenance was all manual</p>
</article>
<a class="abs btn-blue" style="left:486px;top:2441px;width:230px;height:50px">See All Project</a>

<!-- expertise -->
<section class="abs exp-band"></section>
<div class="abs tag" style="left:393px;top:2596px;width:416px;height:58px;background:#d7dbf0"></div>
<h2 class="abs h-section center" style="left:0;top:2596px;width:1200px;font-size:50px;line-height:58px">OUR EXPERTISE</h2>
<p class="abs lead center" style="left:300px;top:2672px;width:600px">We provide expert mechanical design, CAD engineering, and manufacturing ready solutions for products of all complexities.</p>

<div class="abs exp-card" style="left:145px">
  <div class="disc"><svg width="48" height="48" viewBox="0 0 48 48" fill="none" stroke="#fff" stroke-width="2.2"><rect x="12" y="8" width="24" height="8" rx="2"/><path d="M8 34h32v6H8zM14 34V22h20v12"/><path d="M24 24l5 3v5l-5 3-5-3v-5z"/></svg></div>
  <h3>Bespoke Product Design</h3>
  <p>Innovative design from concept through the full development life cycle</p>
</div>
<div class="abs exp-card" style="left:453px">
  <div class="disc"><svg width="48" height="48" viewBox="0 0 48 48" fill="none" stroke="#fff" stroke-width="2.2"><rect x="6" y="10" width="30" height="28" rx="2"/><path d="M21 16l6 3.5v7L21 30l-6-3.5v-7z"/><path d="M36 14h6v24h-6M10 32h6"/></svg></div>
  <h3>3D Modelling and Drawings</h3>
  <p>We create 3D CAD, 2D engineering drawings and photorealistic renders</p>
</div>
<div class="abs exp-card" style="left:760px">
  <div class="disc"><svg width="48" height="48" viewBox="0 0 48 48" fill="none" stroke="#fff" stroke-width="2.2"><path d="M8 10h10v6H8zM13 16v22M8 38h10"/><path d="M24 8v32"/><circle cx="35" cy="24" r="5"/><path d="M35 14v4M35 30v4M25 24h4M41 24h4"/></svg></div>
  <h3>Design for Manufacture</h3>
  <p>Creating designs optimised for proto-type and production manufacture</p>
</div>
<a class="abs btn-blue" style="left:486px;top:3072px;width:230px;height:48px">View All Expertise</a>

<svg class="abs" style="left:0;top:3125px" width="1200" height="125" viewBox="0 0 1200 125" preserveAspectRatio="none">
  <rect width="1200" height="20" fill="#eceaee"/>
  <path d="M0 10 C350 80 800 110 1200 30 V125 H0Z" fill="#3c3f4a"/>
  <path d="M0 10 C300 55 700 90 1200 40 V50 C800 110 300 105 0 50Z" fill="#2f58ec"/>
  <path d="M0 50 C300 105 800 110 1200 50 V30 C1200 30 1200 30 1200 30" fill="#3c3f4a"/>
  <path d="M0 56 C350 125 800 130 1200 58 V125 H0Z" fill="#ffffff"/>
</svg>

<!-- feedback -->
<div class="abs tag" style="left:328px;top:3373px;width:544px;height:52px"></div>
<h2 class="abs h-section center" style="left:0;top:3313px;width:1200px;font-size:52px;line-height:60px">FEEDBACK FROM SOME OF OUR<br>RECENT CUSTOMERS</h2>
<p class="abs lead center" style="left:320px;top:3443px;width:560px">Real feedback from clients who trust us to deliver high-quality mechanical design and engineering solutions.</p>

<div class="abs arrow prev" style="left:63px;top:3722px"><svg width="16" height="16" viewBox="0 0 16 16" fill="none" stroke="#1c1d33" stroke-width="2.4"><path d="M10 2 4 8l6 6"/></svg></div>
<div class="abs arrow next" style="left:1080px;top:3722px"><svg width="16" height="16" viewBox="0 0 16 16" fill="none" stroke="#2f58ec" stroke-width="2.4"><path d="m6 2 6 6-6 6"/></svg></div>

<article class="abs review" style="left:145px">
  <div class="badge"></div>
  <div class="stars">★★★★★</div>
  <blockquote>"Owen is able to bridge the gap between what management want and what manufacturing can deliver. In the field of Casting his intuition for the process and knowledge of casting technical nuances means he is able to push both the design and guide manufacturers to produce excellent results."</blockquote>
  <div class="avatar" role="img" aria-label="Portrait of reviewer"></div>
  <div class="who">Tom Harlow<br>Design Engineer</div>
</article>
<article class="abs review" style="left:458px">
  <div class="badge"></div>
  <div class="stars">★★★★★</div>
  <blockquote>"Owen is able to bridge the gap between what management want and what manufacturing can deliver. In the field of Casting his intuition for the process and knowledge of casting technical nuances means he is able to push both the design and guide manufacturers to produce excellent results."</blockquote>
  <div class="avatar" role="img" aria-label="Portrait of reviewer"></div>
  <div class="who">Nadia Fenwick<br>Client</div>
</article>
<article class="abs review" style="left:771px">
  <div class="badge"></div>
  <div class="stars">★★★★★</div>
  <blockquote>Owen's support, patience and thorough explanation of the technical challenges through the complex development process allowed me as the Project Manager to confidently manage both the supplier and the customers' expectations daily from an informed and knowledgeable position and made my job so much easier</blockquote>
  <div class="avatar" role="img" aria-label="Portrait of reviewer"></div>
  <div class="who">Gareth Lowe<br>Project Manager</div>
</article>

<!-- footer -->
<footer class="abs footer">
  <div class="abs" style="left:145px;top:30px;display:flex;flex-direction:column;align-items:flex-start">
    <div style="width:38px;height:38px;border-radius:50%;background:var(--blue);margin-left:26px;margin-bottom:6px"></div>
    <div style="font-size:30px;font-weight:600;color:#fff;letter-spacing:3px;line-height:1">valtro</div>
    <div style="font-size:8px;font-weight:600;color:var(--blue-soft);letter-spacing:.6px;margin-top:3px">MECHANICAL DESIGN</div>
  </div>
  <p class="abs" style="left:145px;top:147px;width:340px;font-size:12px;line-height:19px">Precision mechanical design and engineering consultancy delivering innovative solutions for complex challenges.</p>
  <div class="abs" style="left:612px;top:102px">
    <h4>Quick Links</h4>
    <a href="#" style="margin-top:18px">Services</a>
    <a href="#" style="margin-top:12px">Portfolio</a>
    <a href="#" style="margin-top:11px">About</a>
    <a href="#" style="margin-top:11px">Contact</a>
  </div>
  <div class="abs" style="left:847px;top:102px">
    <h4>Legal</h4>
    <a href="#" style="margin-top:18px">Privacy Policy</a>
    <a href="#" style="margin-top:12px">Terms of Service</a>
  </div>
  <div class="abs" style="left:145px;top:258px;width:912px;height:1px;background:#3a3b55"></div>
  <p class="abs" style="left:145px;top:281px;font-size:11px">© 2024 Valtro Build. All rights reserved.</p>
  <p class="abs" style="left:917px;top:281px;font-size:11px">Built with precision and care</p>
</footer>

</body>
</html>
```